Semi completed website for an online chocolate shop to be completed

We have an existing logo and chocolate images. We want a modern, attractive and functional website. The aim is to sell our chocolate products so eCommerce is a must. Needs to be compatible with mobile devices. We need SEO optimisation and obviously want to get onto the first page for many searches. We specialise in vegan friendly chocolate, organic, etc.
Updates

Target Market(s)

People wanting to buy niche chocolates (vegan friendly, etc).

Industry/Entity Type

Chocolate Company

Coding

Coded - Design and coding required

Number of Pages Required

4 page

Font styles to use
Script

Colors
f68d4d
fee18a

Requirements
Must have
• The website must include attractive looking graphics, photos, and nice layout. The aim of the website is to Ecommerce and to provide a professional image for our brand, Velvet Cocoa.
Nice to have
• About Us, Shop, Home Page, Contact

```html
<!DOCTYPE html>
<html lang="en">
<head>
<meta charset="utf-8">
<title>Checkout – Velvet Cocoa</title>
<link rel="stylesheet" href="https://fonts.googleapis.com/css2?family=Noto+Serif:wght@400;700&display=swap">
<style>
  :root {
    --bar: #2b2b2b;
    --footer: #0d0d0d;
    --page: #ffffff;
    --card-border: #ececec;
    --text: #333333;
    --placeholder: #bdbdbd;
    --field: #f6f6f6;
    --field-border: #eeeeee;
    --accent: #d98a3e;
    --required: #d04848;
    --rule: #e4e4e4;
    --button: #2e2e2e;
  }
  * { box-sizing: border-box; margin: 0; padding: 0; }
  html, body { width: 1035px; height: 1200px; overflow: hidden; }
  body {
    position: relative;
    background: var(--page);
    font-family: "Noto Serif", Georgia, serif;
    color: var(--text);
    font-size: 11.5px;
  }
  a { color: var(--accent); text-decoration: none; }

  .top-bar {
    position: absolute; left: 0; top: 0; width: 1035px; height: 57px;
    background: var(--bar);
  }
  .top-bar .back-link {
    position: absolute; left: 112px; top: 20px;
    color: #ffffff; font-size: 11.5px;
  }

  .checkout-card {
    position: absolute; left: 107px; top: 102px; width: 821px; height: 986px;
    border: 1px solid var(--card-border);
  }
  .notices { position: absolute; left: 20px; top: 22px; line-height: 17px; }

  .billing { position: absolute; left: 20px; top: 86px; width: 379px; }
  .section-title {
    font-size: 15px; font-weight: 400; letter-spacing: 0.3px;
    text-transform: uppercase; margin-bottom: 16px; line-height: 20px;
  }
  .name-row { display: flex; justify-content: space-between; }
  .name-row .field { width: 179px; }
  .field { margin-bottom: 18px; }
  .field label { display: block; font-weight: 700; font-size: 11px; line-height: 15px; }
  .field .req { color: var(--required); font-weight: 400; }
  .input {
    height: 32px; background: var(--field); border: 1px solid var(--field-border);
    padding: 0 8px; line-height: 30px; color: var(--placeholder); font-size: 10.5px;
    position: relative;
  }
  .input + .input { margin-top: 8px; }
  .select { color: var(--text); }
  .select svg { position: absolute; right: 8px; top: 13px; }
  .create-account { margin-top: 16px; line-height: 15px; }
  .additional { margin-top: 20px; }
  .additional .section-title { margin-bottom: 12px; }
  .textarea { height: 109px; line-height: 18px; padding-top: 6px; }
  .textarea svg { position: absolute; right: 3px; bottom: 3px; }

  .order { position: absolute; left: 446px; top: 86px; width: 328px; }
  .order-table { width: 100%; border-collapse: collapse; }
  .order-table th {
    font-size: 10px; font-weight: 700; text-transform: uppercase; text-align: left;
    padding: 4px 0 14px; border-bottom: 1px solid var(--rule);
  }
  .order-table th:last-child, .order-table td:last-child { text-align: right; }
  .order-table td { font-size: 10.5px; padding: 5px 0 6px; line-height: 15px; }
  .order-table tbody tr:first-child td { padding-top: 12px; }
  .order-table tbody tr:last-child td { padding-bottom: 12px; }
  .order-table .qty { font-weight: 700; }
  .order-table tfoot th, .order-table tfoot td {
    border-top: 1px solid var(--rule); padding: 9px 0 8px; font-size: 11px;
    text-transform: none; font-weight: 700;
  }
  .order-table tfoot td { font-size: 15px; font-weight: 400; }
  .order-table tfoot tr:last-child th, .order-table tfoot tr:last-child td { border-bottom: 1px solid var(--rule); }
  .order-table .grand { color: var(--accent); }

  .payment-note { margin-top: 28px; line-height: 17px; font-size: 10.5px; }
  .place-order {
    display: inline-block; margin-top: 12px; width: 96px; height: 31px; line-height: 31px;
    background: var(--button); color: #ffffff; font-size: 9.5px; text-align: center;
    text-transform: uppercase; border: 1px solid #111;
  }

  .site-footer {
    position: absolute; left: 0; top: 1133px; width: 1035px; height: 67px;
    background: var(--footer);
  }
  .footer-nav { position: absolute; left: 108px; top: 15px; color: #d8d8d8; font-size: 9.5px; }
  .footer-nav span { color: #777; padding: 0 4px; }
  .copyright { position: absolute; left: 108px; top: 40px; color: #6c6c6c; font-size: 8.5px; }
  .newsletter {
    position: absolute; left: 669px; top: 24px; width: 259px; height: 18px;
    border-bottom: 1px solid #555; color: #7d7d7d; font-size: 8.5px;
  }
  .newsletter svg { position: absolute; right: 5px; top: 1px; }
</style>
</head>
<body>
  <header class="top-bar">
    <a class="back-link" href="#">‹ Back to Homepage</a>
  </header>

  <main class="checkout-card">
    <div class="notices">
      <p>Returning customer? <a href="#">Click here to login</a></p>
      <p>Have a coupon? <a href="#">Click here to enter your code</a></p>
    </div>

    <section class="billing">
      <h2 class="section-title">Billing Details</h2>
      <div class="name-row">
        <div class="field"><label>First name <span class="req">*</span></label><div class="input"></div></div>
        <div class="field"><label>Last name <span class="req">*</span></label><div class="input"></div></div>
      </div>
      <div class="field"><label>Company name (optional)</label><div class="input"></div></div>
      <div class="field"><label>Country <span class="req">*</span></label>
        <div class="input select">Australia<svg width="7" height="5" viewBox="0 0 7 5"><path d="M0 0h7L3.5 5z" fill="#555"/></svg></div>
      </div>
      <div class="field"><label>Street address <span class="req">*</span></label>
        <div class="input">House number and street name</div>
        <div class="input">Apartment, suite, unit etc. (optional)</div>
      </div>
      <div class="field"><label>Suburb <span class="req">*</span></label><div class="input"></div></div>
      <div class="field"><label>State <span class="req">*</span></label>
        <div class="input select"><svg width="7" height="5" viewBox="0 0 7 5"><path d="M0 0h7L3.5 5z" fill="#555"/></svg></div>
      </div>
      <div class="field"><label>Postcode <span class="req">*</span></label><div class="input"></div></div>
      <div class="field"><label>Phone <span class="req">*</span></label><div class="input"></div></div>
      <div class="field"><label>Email address <span class="req">*</span></label><div class="input"></div></div>
      <p class="create-account">Create an account?</p>

      <div class="additional">
        <h2 class="section-title">Additional Information</h2>
        <div class="field"><label>Order notes (optional)</label>
          <div class="input textarea">Notes about your order, e.g. special notes for delivery.
            <svg width="8" height="8" viewBox="0 0 8 8"><path d="M8 1L1 8M8 5L5 8" stroke="#999" stroke-width="1"/></svg>
          </div>
        </div>
      </div>
    </section>

    <section class="order">
      <h2 class="section-title">Your Order</h2>
      <table class="order-table">
        <thead><tr><th>Product</th><th>Total</th></tr></thead>
        <tbody>
          <tr><td>Spice Cocoa Orbs <span class="qty">× 1</span></td><td>$9.95</td></tr>
          <tr><td>Ginger Cocoa Orbs <span class="qty">× 1</span></td><td>$9.95</td></tr>
          <tr><td>Chilli Cocoa Orbs <span class="qty">× 1</span></td><td>$9.95</td></tr>
        </tbody>
        <tfoot>
          <tr><th>Subtotal</th><td>$29.85</td></tr>
          <tr><th>Total</th><td class="grand">$29.85</td></tr>
        </tfoot>
      </table>
      <p class="payment-note">Sorry, it seems that there are no available payment methods for your state. Please contact us if you require assistance or wish to make alternate arrangements.<br>Your personal data will be used to process your order, support your experience throughout this website, and for other purposes described in our <a href="#">privacy policy</a>.</p>
      <a class="place-order" href="#">Place Order</a>
    </section>
  </main>

  <footer class="site-footer">
    <nav class="footer-nav">Our Products<span>|</span>Our Story<span>|</span>Our Blog</nav>
    <p class="copyright">Copyright Velvet Cocoa Co 2018. All Rights Reserved.</p>
    <div class="newsletter">Enter your email to join our mailing list
      <svg width="11" height="8" viewBox="0 0 11 8"><rect x="0.5" y="0.5" width="10" height="7" fill="none" stroke="#999"/><path d="M0.5 0.5l5 4 5-4" fill="none" stroke="#999"/></svg>
    </div>
  </footer>
</body>
</html>
```